Design 2 8x10 one page sales brochures for TELNIQ, a cloud service provider.

We’re open to fun and creative, yet must be clean, bold and professional.

***The winning designer will also be hired to design a handful of other brochures for us after the contest***

We understand the value of feedback and will work closely with every design to create the perfect sales brochure!

Should be printer friendly, primarily white so doesn’t consume a lot of printer ink
Colors - grey, black, light blue, llight green
We are a fun, easy to work with technology company and the brochures need to reflect taht.

Don't hesitate to ask any questions, thanks!

We need two designs, each one page 8x10"
#1 Why we're Zip
#2 TELNIQTalk

Target Market(s)

Small and medium sized business owners

Industry/Entity Type

Telecommunications

Font styles to use
Sans Serif

Requirements
Must have
• Clean, professional designs. We're a fun tech company.
• Visually appealing
Nice to have
• graphs, charts, diagrams, etc
Should not have
• not sure.

```html
<!DOCTYPE html>
<html lang="en">
<head>
<meta charset="utf-8">
<title>TELNIQ Sales Brochure</title>
<link href="https://fonts.googleapis.com/css2?family=Montserrat:wght@900&family=Figtree:wght@300;400;600;800&display=swap" rel="stylesheet">
<style>
:root{
  --backdrop:#3a393a;
  --paper:#ffffff;
  --navy:#0b4a7a;
  --navy-deep:#073a63;
  --brand-blue:#1a63a0;
  --ink-blue:#0d4d85;
  --grey-text:#6b6b6b;
  --dark-text:#555555;
  --sky-top:#7fb3cc;
  --sky-mid:#a9cbdc;
  --cloud:#eef4f8;
}
*{margin:0;padding:0;box-sizing:border-box}
html,body{width:1200px;height:1200px;overflow:hidden;background:var(--backdrop)}
body{font-family:"Figtree",sans-serif;font-weight:300;color:var(--grey-text)}
.brochure{position:absolute;left:153px;top:36px;width:909px;height:1138px;background:var(--paper);overflow:hidden}
.header-band{position:absolute;left:0;top:0;width:100%;height:124px;
  background:linear-gradient(100deg,#0c5a95 0%,var(--navy) 40%,var(--navy-deep) 100%);
  display:flex;align-items:center;justify-content:center}
.headline{font-family:"Montserrat",sans-serif;font-weight:900;color:#fff;font-size:26.5px;letter-spacing:-1.6px;white-space:nowrap}
.col{position:absolute}
.section-title{font-weight:400;color:var(--brand-blue);font-size:22px;line-height:28px}
.body-copy{font-size:17px;line-height:22.8px;color:var(--grey-text)}
.intro-left{left:57px;top:163px;width:370px}
.intro-left .body-copy{margin-top:23px}
.intro-right{left:464px;top:163px;width:400px}
.sky-band{position:absolute;left:0;top:369px;width:100%;height:288px;
  background:radial-gradient(ellipse 45% 60% at 72% 50%,#f4f8fb 0%,rgba(230,239,245,.85) 35%,rgba(169,203,220,0) 75%),
  radial-gradient(ellipse 30% 40% at 40% 20%,rgba(240,246,250,.8),rgba(240,246,250,0) 70%),
  linear-gradient(180deg,var(--sky-top),var(--sky-mid))}
.simplicity-box{position:absolute;left:45px;top:77px;width:530px;height:192px;background:rgba(242,246,249,.88);padding:26px 0 0 35px}
.simplicity-title{font-size:24px;line-height:30px;color:var(--dark-text)}
.simplicity-title strong{font-weight:400;color:var(--ink-blue)}
.perks{list-style:none;margin-top:-1px}
.perks li{font-size:22px;line-height:28.4px;font-weight:400;color:var(--dark-text)}
.perks li::before{content:"•";color:#5a8fbf;font-size:16px;margin-right:8px;position:relative;top:-2px}
.network{left:57px;top:705px;width:400px}
.network .accent{color:var(--brand-blue)}
.products{left:464px;top:705px;width:400px}
.product-list{list-style:none;margin-top:4px}
.product{display:flex;align-items:center;height:50px}
.product .icon{width:47px;height:47px;flex:none}
.product span{margin-left:9px;color:var(--ink-blue);font-size:18px;line-height:22px;font-weight:400}
.footer-band{position:absolute;left:0;top:994px;width:100%;height:144px;
  background:radial-gradient(ellipse 60% 70% at 50% 100%,rgba(245,248,251,.9),rgba(245,248,251,0) 75%),
  linear-gradient(180deg,#b8d3e2,#dbe8f0)}
.cta{position:absolute;left:57px;top:38px;font-size:24px;font-weight:400;color:var(--brand-blue);white-space:nowrap}
.cta b{font-weight:800;color:var(--ink-blue)}
.contacts{position:absolute;top:70px;font-size:21px;white-space:nowrap;color:var(--ink-blue);font-weight:400}
.contacts.email{left:99px}
.contacts.web{left:383px;font-weight:800}
.contacts.phone{left:668px}
</style>
</head>
<body>
<main class="brochure">
  <header class="header-band">
    <h1 class="headline">YOUR BUSINESS COMMUNICATIONS DON’T HAVE TO BE LAME</h1>
  </header>

  <section class="col intro-left">
    <h2 class="section-title">Radically Simple Cloud</h2>
    <p class="body-copy">Telniq delivers customized cloud solutions to enterprises and small businesses with the highest level of value, integrity, service, and support - radically changing your ability to communicate and compete in the market</p>
  </section>
  <section class="col intro-right">
    <p class="body-copy">100+ years of collective experience activating over 1M user seats, working with some of the largest organizations in the world. We leveraged our experiences to build an innovative suite of cloud offerings and features, allowing us to build custom solutions based on unique and changing customer needs.</p>
  </section>

  <section class="sky-band" role="img" aria-label="Photo of white cumulus clouds in a pale blue sky">
    <div class="simplicity-box">
      <p class="simplicity-title">What puts the zip in Telniq - <strong>Simplicity</strong></p>
      <ul class="perks">
        <li>No contracts</li>
        <li>No upfront costs or hidden fees</li>
        <li>Free installation</li>
        <li>Free lifetime training &amp; support</li>
      </ul>
    </div>
  </section>

  <section class="col network">
    <h2 class="section-title">Crazy Insane Disaster Proof Network (CIDPN):</h2>
    <p class="body-copy">The only way our network is going down if if a meteor shower simultaneously wipes out our 3 geographical redundant data centers. The statistical likelihood of that happening is virtually non-existent.<br>Make your business’s communications not lame system phone system not lame with TELNIQTalk: <span class="accent">a radically simple way to communicate!</span></p>
  </section>

  <section class="col products">
    <p class="body-copy">TELNIQ’s radical cloud solutions are setting the new standard for enterprise grade cloud:</p>
    <ul class="product-list">
      <li class="product">
        <svg class="icon" viewBox="0 0 48 48" fill="none" stroke="#1a63a0" stroke-width="1.3"><circle cx="24" cy="24" r="23"/><rect x="24" y="12" width="8" height="12" rx="4" transform="rotate(40 28 18)"/><path d="M24 23 L15 34 L17 36 L27 27"/></svg>
        <span>TELNIQTalk</span>
      </li>
      <li class="product">
        <svg class="icon" viewBox="0 0 48 48" fill="none" stroke="#1a63a0" stroke-width="1.3"><circle cx="24" cy="24" r="23"/><path d="M15 26 V22 a9 9 0 0 1 18 0 V26"/><rect x="13" y="24" width="4" height="8" rx="2"/><rect x="31" y="24" width="4" height="8" rx="2"/><path d="M33 32 Q33 37 26 37"/></svg>
        <span>TELNIQCallCenter</span>
      </li>
      <li class="product">
        <svg class="icon" viewBox="0 0 48 48" fill="none" stroke="#1a63a0" stroke-width="1.3"><circle cx="24" cy="24" r="23"/><circle cx="24" cy="17" r="3"/><circle cx="15" cy="21" r="2.6"/><circle cx="33" cy="21" r="2.6"/><path d="M19 28 a5 5 0 0 1 10 0 M10 31 a5 5 0 0 1 9 -2 M29 29 a5 5 0 0 1 9 2 M12 33 H36"/></svg>
        <span>TELNIQMeetings</span>
      </li>
      <li class="product">
        <svg class="icon" viewBox="0 0 48 48" fill="none" stroke="#1a63a0" stroke-width="1.3"><circle cx="24" cy="24" r="23"/><path d="M16 33 L17 28 a9 9 0 1 1 4 4 Z"/></svg>
        <span>TELNIQApps (mobile,<br>desktop, web)</span>
      </li>
    </ul>
  </section>

  <footer class="footer-band" role="img" aria-label="Soft photo of pale clouds behind the contact details">
    <p class="cta">Make your business communications not lame, contact <b>TELNIQ</b> today!</p>
    <p class="contacts email">sales@telniq.com</p>
    <p class="contacts web">www.telniq.com</p>
    <p class="contacts phone">555-010-1999</p>
  </footer>
</main>
</body>
</html>
```